Information poster for parquet showroom

We are a parquet shop from germany and need some information poster for our showroom, to show our costumers some important information about parqut directly. The three posters are about reasons for parquet, and there are two types of paper on the subject. We would like to place the posters in a wooden frame. The design should be modern but simple. Enclosed I send you some of my ideas but it does not have to be like this. Can be completely different. I also send you some pictures of our showroom. 1st poster: Why parquet (dimension: 90x130 cm) Why parquet? - brings nature into your home - ecologically sustainable raw material - pleasantly warm - timeless% 26amp; high quality optics - durable% 26amp; reparable flooring - improved indoor climate - unique ride 2. Advantages oiled - tangible wood structure - natural appearance - scratches less present - partial repair possible advantage varnished - very easy-care - classic% 26amp; elegant appearance - protection against dirt and moisture - variable gloss level 3. Poster: overview of the hardness of different kinds of wood (dimension: 67x130 cm) wood hardness according to Brinell in N / mm² maple europ. 28 maple canadian. 35 birch 27 beech 33 oak 34 alder 17 ash 37 doussie 42 spruce 12 kambala 30 chestnut 18 pine 20 cherry european. 31 Larch 19 Merbau 44 Robinia 48 Sucupira 57 Elm 30 Wenge 45

```html
<!DOCTYPE html>
<html lang="en">
<head>
<meta charset="utf-8">
<title>Why Parquet?</title>
<link href="https://fonts.googleapis.com/css2?family=Anton&display=swap" rel="stylesheet">
<style>
  :root {
    --bg-dark: #0f0f0f;
    --bg-mid: #1e1e1e;
    --bg-light: #2f2f2f;
    --text-light: #e6e6e6;
    --text-grey: #6e6e6e;
    --frame: #d9d9d9;
    --bullet-front: #b4b4b4;
    --bullet-back: #5a5a5a;
  }
  html, body {
    margin: 0;
    padding: 0;
    overflow: hidden;
    background: var(--bg-dark);
  }
  .poster {
    position: relative;
    width: 831px;
    height: 1200px;
    overflow: hidden;
    font-family: "Anton", "Impact", sans-serif;
    color: var(--text-light);
  }
  .poster-background {
    position: absolute;
    inset: 0;
    background:
      radial-gradient(ellipse at 75% 30%, #262626 0%, transparent 55%),
      linear-gradient(170deg, var(--bg-mid) 0%, var(--bg-dark) 40%, var(--bg-mid) 70%, var(--bg-light) 100%);
  }
  .poster-frame {
    position: absolute;
    left: 17px;
    top: 17px;
    right: 17px;
    bottom: 17px;
    border: 2px solid var(--frame);
  }
  .headline-why {
    position: absolute;
    left: 142px;
    top: 62px;
    margin: 0;
    font-size: 190px;
    line-height: 1;
    font-weight: 400;
    color: var(--text-light);
    transform: rotate(-4deg);
    transform-origin: left top;
  }
  .headline-parquet {
    position: absolute;
    left: 122px;
    top: 300px;
    margin: 0;
    font-size: 112px;
    line-height: 1;
    font-weight: 400;
    color: var(--text-grey);
    transform: rotate(-8deg);
    transform-origin: left top;
  }
  .headline-mark {
    position: absolute;
    left: 556px;
    top: 176px;
    margin: 0;
    font-size: 300px;
    line-height: 1;
    color: var(--text-light);
    transform: rotate(-6deg);
  }
  .benefit-list {
    position: absolute;
    left: 68px;
    top: 560px;
    margin: 0;
    padding: 0;
    list-style: none;
  }
  .benefit-item {
    position: relative;
    height: 84.5px;
    padding-left: 49px;
    font-size: 38px;
    line-height: 56px;
    letter-spacing: 0.2px;
    white-space: nowrap;
  }
  .benefit-item::before,
  .benefit-item::after {
    content: "";
    position: absolute;
    width: 16px;
    height: 16px;
  }
  .benefit-item::before {
    left: 6px;
    top: 26px;
    background: var(--bullet-back);
  }
  .benefit-item::after {
    left: 0;
    top: 20px;
    background: var(--bullet-front);
  }
</style>
</head>
<body>
  <main class="poster">
    <div class="poster-background" role="img" aria-label="Dark grey low-poly triangle texture"></div>
    <div class="poster-frame"></div>

    <h1 class="headline">
      <span class="headline-why">WHY</span>
      <span class="headline-parquet">PARQUET</span>
      <span class="headline-mark">?</span>
    </h1>

    <ul class="benefit-list">
      <li class="benefit-item">BRINGS NATURE INTO YOUR HOME</li>
      <li class="benefit-item">ECOLOGICALLY SUSTAINABLE RAW MATERIAL</li>
      <li class="benefit-item">PLEASANTLY WARM</li>
      <li class="benefit-item">TIMELESS% 26AMP; HIGH QUALITY OPTICS</li>
      <li class="benefit-item">DURABLE% 26AMP; REPARABLE FLOORING</li>
      <li class="benefit-item">IMPROVED INDOOR CLIMATE</li>
      <li class="benefit-item">UNIQUE RIDE</li>
    </ul>
  </main>
</body>
</html>
```